TARPLOAD business card design

TARPLOAD is a manufacturer of skip bags supplying both the domestic and commercial market. We wish to convey core characteristics of strength, professionalism and reliability to our customers. We are after a business card that uses our company colours of black and yellow as well as incorporating our logo. Our customers are predominantly in the construction or hardware industry. It is important the cards are professional as we are a small company wishing to appear larger than we actually are. more info on the company and product available at www.tarpload-example.com.au

Target Market(s)

hardware buyers, contruction company owners

Industry/Entity Type

Construction

Requirements
Must have
• company colours of black and yellow - No other colours or variation of yellow black. our company logo. card design must convey "tough"
• Card design must be landscape
• Details to be included on the card are:
• Name and Tiltle
• Phone number : 1300 41 62 53
• Mobile: 0452 718 903
• Fax: 03 9617 4852
• email: dale.hendry@tarpload-example.com.au
• address: PO Box 517, Kelvindale, VIC,3294
• Text in white when on a black background
Nice to have
• I like the idea of the back of the card being black with lighter circle area in the middle with black logo in the centre. Similar to the attached "iconic" card

```html
<!DOCTYPE html>
<html lang="en">
<head>
<meta charset="utf-8">
<title>TARPLOAD business card – front and back</title>
<link rel="stylesheet" href="https://fonts.googleapis.com/css2?family=Oswald:wght@300;400;700&family=PT+Sans&display=swap">
<style>
  :root {
    --yellow: #f0cb00;
    --yellow-glow: #f6de4a;
    --black: #000000;
    --ink: #231f20;
    --white: #ffffff;
    --label: #1e1a0e;
  }
  * { margin: 0; padding: 0; box-sizing: border-box; }
  html, body {
    width: 1187px; height: 1200px; overflow: hidden;
    background: var(--white);
  }
  .board { position: relative; width: 1187px; height: 1200px; }

  .card-sheet {
    position: absolute; left: 30px; width: 852px;
    background: var(--white);
    box-shadow: 6px 7px 9px rgba(0,0,0,.45);
  }
  .card-sheet--front { top: 17px; height: 509px; }
  .card-sheet--back  { top: 620px; height: 510px; }

  .card {
    position: absolute; left: 50px; width: 749px; height: 428px;
    overflow: hidden;
  }
  .card-sheet--front .card { top: 35px; background: var(--yellow); }
  .card-sheet--back .card  { top: 46px; background: var(--black); }

  /* front */
  .top-rule {
    position: absolute; left: 0; top: 21px; width: 100%; height: 11px;
    background: var(--black);
  }
  .person { position: absolute; left: 40px; top: 50px; color: var(--black); }
  .person__name {
    font: 700 36px/1 "Oswald", sans-serif; letter-spacing: .5px;
    padding-left: 4px;
  }
  .person__title {
    font: 300 20px/1.3 "Oswald", sans-serif; margin-top: 2px;
  }
  .brand-name {
    position: absolute; left: 472px; top: 196px; width: 208px;
    font: 700 50px/1 "Oswald", sans-serif; color: var(--ink);
    text-align: center; letter-spacing: 1px;
  }
  .brand-rule {
    position: absolute; left: 472px; top: 180px; width: 208px; height: 9px;
    background: var(--ink);
  }
  .address-band {
    position: absolute; left: 0; top: 331px; width: 100%; height: 79px;
    background: var(--black); color: var(--white);
    display: flex; flex-direction: column; justify-content: center;
    padding-left: 179px;
    font: 300 17px/24px "Oswald", sans-serif;
  }

  /* back */
  .spotlight {
    position: absolute; left: 0; top: 0; width: 100%; height: 332px;
    background: radial-gradient(circle 270px at 376px 175px,
      #b4b4b4 0%, #8a8a8a 35%, #3a3a3a 72%, var(--black) 100%);
  }
  .back-brand-rule {
    position: absolute; left: 216px; top: 190px; width: 326px; height: 15px;
    background: var(--ink);
  }
  .back-brand-name {
    position: absolute; left: 196px; top: 212px; width: 366px;
    font: 700 80px/1 "Oswald", sans-serif; color: var(--ink);
    text-align: center; letter-spacing: 2px;
  }
  .back-band {
    position: absolute; left: 0; top: 332px; width: 100%; height: 66px;
    background: radial-gradient(ellipse 280px 60px at 376px 10px,
      var(--yellow-glow) 0%, var(--yellow) 100%);
  }
  .back-foot {
    position: absolute; left: 0; top: 398px; width: 100%; height: 30px;
    background: radial-gradient(ellipse 260px 40px at 376px 0,
      #2a2a2a 0%, var(--black) 100%);
  }

  .side-label {
    position: absolute; font: 400 71px/1 "PT Sans", sans-serif;
    color: var(--label);
  }
  .side-label--front { left: 961px; top: 232px; }
  .side-label--back  { left: 966px; top: 816px; }
</style>
</head>
<body>
<main class="board">

  <section class="card-sheet card-sheet--front" aria-label="Card front">
    <div class="card">
      <div class="top-rule"></div>
      <div class="person">
        <p class="person__name">Name</p>
        <p class="person__title">Designation</p>
      </div>
      <div class="brand-rule"></div>
      <p class="brand-name">TARPLOAD</p>
      <div class="address-band">
        <p>Mock add. will come here. Mock add. will come here.</p>
        <p>Mock add. will come here. Mock add. will come here.</p>
      </div>
    </div>
  </section>
  <p class="side-label side-label--front">Front</p>

  <section class="card-sheet card-sheet--back" aria-label="Card back">
    <div class="card">
      <div class="spotlight"></div>
      <div class="back-brand-rule"></div>
      <p class="back-brand-name">TARPLOAD</p>
      <div class="back-band"></div>
      <div class="back-foot"></div>
    </div>
  </section>
  <p class="side-label side-label--back">Back</p>

</main>
</body>
</html>
```